KLD Photography Editing & Support Services for Real Estate

We require a double sided A4 flyer to promote our photography services to real estate agencies.
This particular service is targeted to rural areas where reliable, professional and highly skilled photographers are difficult to source. We teach the agent how to photograph, they upload files to a server and we take care of the rest (image editing, quality control and delivery). This will give the agents flexibility with when to shoot and eliminates the stress of managing a photographer / contractor. We offer a 1 day face to face training session and competitive packages for equipment start up.
We would like the flyer to look clean & very professional. The flyer should showcase samples of our work to highlight what can be achieved by using our services. We like the look of a black or dark background behind the text and feel that would look nice with our photographs provided. Otherwise open to your suggestions and ideas.
TEXT FOR FLYER:
Welcome to the KLD Real Estate Photography Editing and Support Service
• Take your real estate business to the next level by providing impressive real estate imagery that makes you stands out from the competition
• Omit the stress of trying to find a good photographer or managing an unreliable one and hence have more time to focus on other aspects of your business
• Showcase your listings with better quality and more impactful photographs than your competitors thereby increasing potential for a quick sale
• Great first impressions matter and you will achieve this by looking and feeling more professional. This will attract and retain more future clients.
HOW IT WORKS
• We understand that your time is valuable, so let us handle the editing and delivery of your images. You shoot, and we take care of the rest.
• Images are edited and delivered within 1 working day
INCLUSIONS:
• Full day face to face training (we come to you) and instructional handbook
• We will teach you everything you need to know about your equipment and how to take stunning real estate photographs
• Service turnaround within 1 working day
• Free HELP desk service Mon-Fri
• 12 month Exclusivity (rural towns only) for a limited time
INVESTMENT
• 99 per listing for us to manage images including editing, quality control and delivery (10 Images)
• Ask us about competitive packages for photography equipment if required
SUMMARY
The KLD Real Estate Photography Editing and Support Service is the perfect solution for busy real estate professionals who want to take their business to the next level. Our service is affordable, flexible, and designed to help you showcase your listings in the best possible light.
Contact us today to learn more about how we can help you.

```html
<!DOCTYPE html>
<html lang="en">
<head>
<meta charset="utf-8">
<title>KLD Real Estate Photography Flyer</title>
<link rel="stylesheet" href="https://fonts.googleapis.com/css2?family=Montserrat:wght@300;400;500;600;700;800&display=swap">
<style>
:root{
  --stage:#8d8d8d;
  --paper:#f5f5f5;
  --ink:#111111;
  --text:#1c1c1c;
  --muted:#777777;
  --rule:#bdbdbd;
  --white:#ffffff;
}
*{box-sizing:border-box;margin:0;padding:0}
html,body{width:800px;height:1200px;overflow:hidden}
body{background:var(--stage);font-family:'Montserrat',sans-serif;color:var(--text)}
.stage{width:800px;height:1200px;display:flex;align-items:center;justify-content:center;gap:14px}
.page{position:relative;width:380px;height:537px;background:linear-gradient(135deg,#fafafa 0%,#efefef 45%,#f8f8f8 60%,#eeeeee 100%);box-shadow:0 4px 14px rgba(0,0,0,.25);overflow:hidden}

.hero{position:relative;height:172px;border-bottom:1.5px solid var(--ink);background:linear-gradient(180deg,#eceae6 0%,#f6f5f2 35%,#e7e2da 75%,#d9d2c6 100%)}
.brand{position:absolute;left:0;right:0;text-align:center;font-weight:300;font-size:13px;letter-spacing:4px;color:var(--muted)}
.hero .brand{top:52px}
.back .brand{top:48px}
.welcome{position:absolute;left:36px;right:36px;top:116px;text-align:center;font-size:10.5px;font-weight:500;line-height:1.45;color:var(--ink)}
.welcome strong{font-weight:800;font-size:14px}
.welcome::before,.welcome::after{content:"";position:absolute;width:20px;height:20px}
.welcome::before{left:-6px;top:-5px;border-left:1px solid var(--ink);border-top:1px solid var(--ink)}
.welcome::after{right:-16px;bottom:-10px;border-right:1px solid var(--ink);border-bottom:1px solid var(--ink)}

.section-title{display:block;width:96px;margin:0 auto;border:1.2px solid var(--ink);background:var(--white);text-align:center;font-size:8.5px;font-weight:700;letter-spacing:.6px;padding:3px 0;color:var(--ink)}
.columns{display:flex;margin:9px 14px 0}
.col{flex:1;list-style:none}
.col+.col{border-left:1px solid var(--rule);margin-left:8px;padding-left:8px}
.col li{position:relative;padding-left:15px;font-size:6.5px;line-height:1.2;margin-bottom:6px}
.tick{position:absolute;left:0;top:50%;width:10px;height:10px;margin-top:-5px}
.divider{height:1px;background:var(--rule);margin:2px 14px 0}

.front .services{margin-top:14px}
.front .how{margin-top:9px}
.photo-row{display:flex;gap:7px;margin:10px 14px 0}
.photo{flex:1;height:83px;box-shadow:0 1px 3px rgba(0,0,0,.35)}
.ph-dusk-house{background:linear-gradient(180deg,#7f9ab8 0%,#b6a7a8 40%,#3b3a36 65%,#5d6b45 100%)}
.ph-coast-cabin{background:linear-gradient(180deg,#a9b5c8 0%,#e7c4b2 40%,#6d8aa0 60%,#3c6b2f 100%)}
.ph-farmhouse{background:linear-gradient(180deg,#8a9cc6 0%,#c9c4d6 35%,#cfc7ba 65%,#e4e2de 100%)}

.back .inclusions{margin-top:95px}
.back .investment{margin-top:10px}
.grid{display:grid;grid-template-columns:repeat(3,1fr);gap:7px;margin:9px 14px 0}
.grid .photo{height:82px}
.ph-bathroom{background:linear-gradient(180deg,#d8d3cc 0%,#cfc6ba 60%,#b08a63 100%)}
.ph-living{background:linear-gradient(180deg,#8a5a32 0%,#2d3a4a 45%,#9b8f84 100%)}
.ph-bedroom{background:linear-gradient(135deg,#e9e6e2 0%,#9aa98e 45%,#f2f0ec 100%)}
.ph-hallway{background:linear-gradient(90deg,#6b4a32 0%,#d9d6d0 50%,#b6b0a6 100%)}
.ph-kitchen{background:linear-gradient(180deg,#5a4030 0%,#ece8e2 40%,#c7a684 100%)}
.ph-lounge{background:linear-gradient(135deg,#2a3140 0%,#4b5566 50%,#1f2229 100%)}
.summary{margin:10px 16px 0;text-align:center;font-size:6.3px;line-height:1.3}
.summary strong{font-weight:700}

.contact-tag{position:absolute;left:50%;bottom:53px;transform:translateX(-50%);background:var(--white);border:1.2px solid var(--ink);padding:3px 6px;font-size:8.5px;font-weight:700;white-space:nowrap;z-index:2;color:var(--ink)}
.back .contact-tag{letter-spacing:.6px}
.footer{position:absolute;left:0;right:0;bottom:0;height:60px;background:var(--ink);display:flex;align-items:center;padding:10px 14px 0}
.footer-item{flex:1;display:flex;flex-direction:column;align-items:center;gap:5px;color:var(--white);font-size:7px;font-weight:700;white-space:nowrap}
.footer-item+.footer-item{border-left:1px solid #555}
.footer-item:first-child{align-items:flex-start}
.footer-item:last-child{align-items:flex-end}
.footer-item .light{font-weight:400}
.icon{width:14px;height:14px}
.footer-item:first-child .icon{margin-left:25px}
.footer-item:last-child .icon{margin-right:25px}
</style>
</head>
<body>
<svg width="0" height="0" style="position:absolute" aria-hidden="true">
  <defs>
    <symbol id="tick" viewBox="0 0 10 10">
      <circle cx="5" cy="5" r="4.5" fill="none" stroke="#111" stroke-width=".8"/>
      <circle cx="5" cy="5" r="3.5" fill="#111"/>
      <path d="M3.3 5.1 4.5 6.2 6.8 3.9" fill="none" stroke="#fff" stroke-width=".9"/>
    </symbol>
    <symbol id="i-person" viewBox="0 0 14 14">
      <circle cx="7" cy="7" r="6.5" fill="#fff"/>
      <circle cx="7" cy="5.5" r="1.8" fill="none" stroke="#111" stroke-width=".9"/>
      <path d="M4.2 10.2c.4-1.6 1.5-2.3 2.8-2.3s2.4.7 2.8 2.3z" fill="none" stroke="#111" stroke-width=".9"/>
    </symbol>
    <symbol id="i-mail" viewBox="0 0 14 14">
      <circle cx="7" cy="7" r="6.5" fill="#fff"/>
      <rect x="3.8" y="4.8" width="6.4" height="4.4" fill="none" stroke="#111" stroke-width=".8"/>
      <path d="M3.8 4.8 7 7.3l3.2-2.5" fill="none" stroke="#111" stroke-width=".8"/>
    </symbol>
    <symbol id="i-phone" viewBox="0 0 14 14">
      <circle cx="7" cy="7" r="6.5" fill="#fff"/>
      <path d="M5 3.8l1.1 1.6-.7.9c.5 1 1.3 1.8 2.3 2.3l.9-.7 1.6 1.1-.6 1.2c-2.7-.2-5-2.5-5.2-5.2z" fill="none" stroke="#111" stroke-width=".8" stroke-linejoin="round"/>
    </symbol>
  </defs>
</svg>

<main class="stage">
  <section class="page front">
    <header class="hero" role="img" aria-label="Bright white open-plan interior with dining table and tall windows">
      <div class="brand">KIERAN DALE</div>
      <h1 class="welcome"><strong>Welcome</strong> to the KLD Real Estate<br>Photography Editing and Support <strong>Services</strong></h1>
    </header>

    <h2 class="section-title services">OUR SERVICES</h2>
    <div class="columns">
      <ul class="col">
        <li><svg class="tick"><use href="#tick"/></svg>Take your real estate business to the next level by providing impressive real estate imagery that makes you stands out from the competition</li>
        <li><svg class="tick"><use href="#tick"/></svg>Omit the stress of trying to find a good photographer or managing an unreliable one and hence have more time to focus on other aspects of your business</li>
      </ul>
      <ul class="col">
        <li><svg class="tick"><use href="#tick"/></svg>Showcase your listings with better quality and more impactful photographs than your competitors thereby increasing potential for a quick sale</li>
        <li><svg class="tick"><use href="#tick"/></svg>Great first impressions matter and you will achieve this by looking and feeling more professional. This will attract and retain more future clients</li>
      </ul>
    </div>
    <div class="divider"></div>

    <h2 class="section-title how">HOW IT WORKS</h2>
    <div class="columns">
      <ul class="col">
        <li><svg class="tick"><use href="#tick"/></svg>We understand that your time is valuable, so let us handle the editing and delivery of your images. You shoot, and we take care of the rest.</li>
      </ul>
      <ul class="col">
        <li><svg class="tick"><use href="#tick"/></svg>Images are edited and delivered within 1 working day</li>
      </ul>
    </div>

    <div class="photo-row">
      <div class="photo ph-dusk-house" role="img" aria-label="Dark timber house at dusk with lit windows and garden path"></div>
      <div class="photo ph-coast-cabin" role="img" aria-label="Black cabin on a grassy clifftop above the ocean at sunset"></div>
      <div class="photo ph-farmhouse" role="img" aria-label="White modern farmhouse with metal roof at twilight"></div>
    </div>

    <div class="contact-tag">Contact Us Today</div>
    <footer class="footer">
      <div class="footer-item"><svg class="icon"><use href="#i-person"/></svg>Kieran Dale</div>
      <div class="footer-item"><svg class="icon"><use href="#i-mail"/></svg><span><span class="light">shoot@</span>kierandale<span class="light">.com.au</span></span></div>
      <div class="footer-item"><svg class="icon"><use href="#i-phone"/></svg>+61 400 555 018</div>
    </footer>
  </section>

  <section class="page back">
    <div class="brand">KIERAN DALE</div>

    <h2 class="section-title inclusions">INCLUSIONS</h2>
    <div class="columns">
      <ul class="col">
        <li><svg class="tick"><use href="#tick"/></svg>Full day face to face training (we come to you) and instructional handbook</li>
        <li><svg class="tick"><use href="#tick"/></svg>We will teach you everything you need to know about your equipment and how to take stunning real estate photographs</li>
      </ul>
      <ul class="col">
        <li><svg class="tick"><use href="#tick"/></svg>Service turnaround within 1 working day</li>
        <li><svg class="tick"><use href="#tick"/></svg>Free HELP desk service (Monday-Friday)</li>
        <li><svg class="tick"><use href="#tick"/></svg>12 month Exclusivity (rural towns only) for a limited time</li>
      </ul>
    </div>
    <div class="divider"></div>

    <h2 class="section-title investment">INVESTMENT</h2>
    <div class="columns">
      <ul class="col">
        <li><svg class="tick"><use href="#tick"/></svg>99 per listing for us to manage images including editing, quality control and delivery (10 Images)</li>
      </ul>
      <ul class="col">
        <li><svg class="tick"><use href="#tick"/></svg>Ask us about competitive packages for photography equipment if required</li>
      </ul>
    </div>

    <div class="grid">
      <div class="photo ph-bathroom" role="img" aria-label="Bathroom with freestanding bath and timber vanity"></div>
      <div class="photo ph-living" role="img" aria-label="Living room under a timber cathedral ceiling"></div>
      <div class="photo ph-bedroom" role="img" aria-label="White bedroom with views over green paddocks"></div>
      <div class="photo ph-hallway" role="img" aria-label="Long hallway with timber bench and framed art"></div>
      <div class="photo ph-kitchen" role="img" aria-label="Open kitchen and dining room with timber beams"></div>
      <div class="photo ph-lounge" role="img" aria-label="Dark lounge with navy sofa and window light"></div>
    </div>

    <p class="summary"><strong>The KLD Real Estate Photography Editing and Support Service</strong> is the perfect solution for busy real estate professionals who want to take their business to the next level. Our service is affordable, flexible and designed to help you showcase your listings in the <strong>best possible light</strong>.</p>

    <div class="contact-tag">CONTACT US TODAY</div>
    <footer class="footer">
      <div class="footer-item"><svg class="icon"><use href="#i-person"/></svg>Kieran Dale</div>
      <div class="footer-item"><svg class="icon"><use href="#i-mail"/></svg><span><span class="light">shoot@</span>kierandale<span class="light">.com.au</span></span></div>
      <div class="footer-item"><svg class="icon"><use href="#i-phone"/></svg>+61 400 555 018</div>
    </footer>
  </section>
</main>
</body>
</html>
```